Looking to Redesign Velmorix.com website

You guys did one of the brochures for velmorix.com and I would like to see if we can go ahead and get an estimate for a redesigned web site for the company. We currently have a couple of pages on velmorix.com which are very much a starter type site.

The new design will need to reflect some of the things discussed in the brochure. It will have flash. Needs to be designed for simple hosting using cpanels.

The site needs to have between 12 and 15 pages with flash pages to move through features. Integrated with twitter like it is now, and contact forms delivered from our CRM along with other interactive features such as subscription to newsletter, etc...

I don't have lots of details on how to proceed yet, but here are some competitor sites:

Can we take a look at potential costs involved in the redo of the site as vague as my description above can permit.

Target Market(s)

Business to Business

Number of Pages Required

5+ page

Font styles to use
Sans Serif

Requirements
Must have
• Must have professional feel. Similar to brochure. and logo.
• Include our story in the discussion.
• embedded links to our CRM for popup contact forms.
• Logo files and 2 types of brochures uploaded.
• Important to keep color scheme
Nice to have
• Flash and some movement
Should not have
• Not sure yet

```html
<!DOCTYPE html>
<html lang="en">
<head>
<meta charset="utf-8">
<title>Velmorix Universal Communications</title>
<link rel="stylesheet" href="https://fonts.googleapis.com/css2?family=Raleway:wght@400;500;600&family=Open+Sans:wght@400;600&display=swap">
<style>
  :root {
    --red: #c9161d;
    --red-deep: #b3121a;
    --ink: #2a2a2a;
    --text: #555555;
    --muted: #777777;
    --icon-grey: #4b4b4b;
    --light: #f1f2f3;
    --footer: #2b2b2b;
    --white: #ffffff;
  }
  * { box-sizing: border-box; margin: 0; padding: 0; }
  html, body { width: 1200px; height: 2449px; overflow: hidden; }
  body { position: relative; background: var(--white); font-family: "Open Sans", Arial, sans-serif; color: var(--text); }
  .heading { font-family: "Raleway", Arial, sans-serif; font-weight: 500; }
  section, header, footer { position: absolute; left: 0; width: 1200px; overflow: hidden; }

  /* Hero */
  .hero { top: 0; height: 560px; border-bottom: 5px solid var(--red); }
  .hero-photo { position: absolute; inset: 0; background: linear-gradient(110deg, #3d5366 0%, #5b7287 35%, #8b98a6 60%, #3a4350 100%); }
  .hero-shade { position: absolute; inset: 0; background: linear-gradient(90deg, rgba(20,35,50,.55) 0%, rgba(20,35,50,.15) 60%, rgba(20,35,50,.25) 100%); }
  .brand { position: absolute; left: 176px; top: 40px; display: flex; align-items: center; gap: 12px; }
  .brand-mark { width: 52px; height: 52px; border-radius: 50%; background: var(--red); }
  .brand-name { font-family: "Raleway", Arial, sans-serif; font-weight: 600; font-size: 26px; color: var(--white); }
  .main-nav { position: absolute; left: 500px; top: 50px; display: flex; gap: 27px; }
  .main-nav a { font-family: "Raleway", Arial, sans-serif; font-size: 14px; font-weight: 500; color: var(--white); text-decoration: none; padding-bottom: 10px; }
  .main-nav a.active { color: var(--red); border-bottom: 2px solid var(--red); }
  .hero-copy { position: absolute; left: 176px; top: 216px; color: var(--white); }
  .hero-kicker { font-size: 32px; letter-spacing: 1px; line-height: 38px; }
  .hero-title { font-size: 47px; letter-spacing: 1px; line-height: 54px; }
  .hero-lead { font-family: "Open Sans", Arial, sans-serif; font-size: 13.5px; line-height: 22px; margin-top: 6px; width: 430px; }
  .slider-dots { display: flex; gap: 6px; margin-top: 24px; }
  .slider-dots span { width: 16px; height: 16px; border-radius: 50%; background: var(--white); }
  .slider-dots span.active { background: transparent; border: 2px solid var(--white); }

  /* About */
  .about { top: 560px; height: 363px; background: linear-gradient(160deg, #f7f7f8 0%, #eceef0 50%, #f5f6f7 100%); text-align: center; }
  .section-title { font-size: 28px; color: var(--ink); letter-spacing: .5px; }
  .about .section-title { margin-top: 50px; }
  .about-text { width: 670px; margin: 18px auto 0; font-size: 11.5px; line-height: 22px; color: var(--muted); }
  .channel-icons { position: absolute; top: 198px; left: 240px; display: flex; gap: 24px; }
  .channel-icons svg { width: 100px; height: 90px; }

  /* Why */
  .why { top: 923px; height: 388px; background: radial-gradient(circle at 35% 40%, #d8272d 0%, var(--red-deep) 70%); color: var(--white); }
  .why-content { position: absolute; left: 181px; top: 76px; width: 410px; }
  .why .section-title { color: var(--white); font-size: 29px; line-height: 36px; margin-bottom: 12px; }
  .why-text { font-size: 11.5px; line-height: 18px; }
  .why-text p + p { margin-top: 8px; }
  .outline-button { display: inline-block; border: 1.5px solid var(--white); color: var(--white); font-size: 11.5px; line-height: 14px; padding: 9px 18px; font-family: "Raleway", Arial, sans-serif; }
  .why .outline-button { margin-top: 16px; margin-left: 2px; }
  .tablet { position: absolute; left: 632px; top: 70px; width: 386px; height: 214px; background: #f6f6f6; border: 2px solid #d9d9d9; border-radius: 14px; }
  .tablet-screen { position: absolute; left: 22px; top: 8px; right: 22px; bottom: 8px; background: linear-gradient(180deg, #eae7e2, #dcd8d0); }

  /* Benefits */
  .benefits { top: 1311px; height: 404px; background: var(--white); }
  .benefits .section-title { text-align: center; margin-top: 56px; font-size: 23px; }
  .benefit { position: absolute; width: 285px; }
  .benefit-icon { position: absolute; left: 0; top: 0; width: 68px; height: 68px; border-radius: 50%; border: 1.5px solid #cfcfcf; display: flex; align-items: center; justify-content: center; }
  .benefit-name { position: absolute; left: 77px; top: 0; font-family: "Raleway", Arial, sans-serif; font-size: 19px; line-height: 24px; color: var(--red); }
  .benefit-text { position: absolute; left: 77px; top: 29px; width: 200px; font-size: 10px; line-height: 15px; color: var(--muted); }
  .view-all { position: absolute; left: 529px; top: 331px; width: 134px; height: 34px; border: 1.5px solid #9a9a9a; border-radius: 18px; text-align: center; line-height: 31px; font-size: 12px; color: #444; font-family: "Raleway", Arial, sans-serif; }

  /* Features */
  .features { top: 1715px; height: 359px; border-top: 1px solid #e4e4e4; }
  .features-photo { position: absolute; left: 0; top: 0; width: 600px; height: 359px; background: linear-gradient(120deg, #8c8f8a 0%, #6c7065 45%, #a5a6a0 100%); }
  .features .section-title { position: absolute; left: 645px; top: 58px; font-size: 24px; color: var(--red); }
  .feature-list { position: absolute; left: 650px; top: 104px; list-style: none; width: 420px; }
  .feature-list li { position: relative; padding-left: 16px; font-size: 11.5px; line-height: 17px; color: #555; margin-bottom: 11px; }
  .feature-list li::before { content: ""; position: absolute; left: 0; top: 5px; width: 6px; height: 6px; border-right: 1.3px solid #888; border-top: 1.3px solid #888; transform: rotate(45deg); }

  /* Newsletter */
  .newsletter { top: 2074px; height: 248px; background: linear-gradient(100deg, #3a3a38 0%, #56544f 45%, #2f2f30 100%); text-align: center; color: var(--white); }
  .newsletter .section-title { color: var(--white); margin-top: 48px; font-size: 24px; letter-spacing: 1px; }
  .newsletter-lead { font-size: 14px; margin-top: 4px; }
  .subscribe-form { position: absolute; left: 367px; top: 137px; width: 482px; height: 41px; background: var(--white); display: flex; align-items: center; }
  .subscribe-form .mail-glyph { margin-left: 10px; }
  .subscribe-form .field { flex: 1; text-align: left; padding-left: 10px; font-size: 13px; color: #888; }
  .subscribe-form .submit { width: 122px; height: 35px; margin-right: 3px; background: var(--red); color: var(--white); font-size: 13.5px; line-height: 35px; font-family: "Raleway", Arial, sans-serif; font-weight: 500; }

  /* Footer */
  .site-footer { top: 2322px; height: 127px; background: var(--footer); color: #d6d6d6; }
  .footer-nav { position: absolute; left: 176px; top: 40px; display: flex; gap: 29px; }
  .footer-nav a { font-family: "Raleway", Arial, sans-serif; color: var(--white); font-size: 14px; text-decoration: none; }
  .copyright { position: absolute; left: 176px; top: 71px; font-size: 11.5px; }
  .social { position: absolute; left: 886px; top: 37px; display: flex; gap: 4px; }
  .social span { width: 30px; height: 30px; border-radius: 50%; border: 1.5px solid var(--white); }
</style>
</head>
<body>

<header class="hero">
  <div class="hero-photo" role="img" aria-label="Photo of business colleagues smiling while using a tablet, with network icons overlaid"></div>
  <div class="hero-shade"></div>
  <div class="brand"><span class="brand-mark"></span><span class="brand-name">velmorix</span></div>
  <nav class="main-nav">
    <a class="active">HOME</a><a>ABOUT</a><a>WHY US</a><a>FEATURES</a><a>ADVANTAGES</a><a>SUPPORT</a>
  </nav>
  <div class="hero-copy heading">
    <div class="hero-kicker">VELMORIX UNIVESAL</div>
    <div class="hero-title">COMMUNICATIONS</div>
    <p class="hero-lead">Aorem ipsum dolor sit amet consectetuer adipiscing elit Nam cursus Morbi ut mi Nullam enim leo egestas id condimentum</p>
    <div class="slider-dots"><span class="active"></span><span></span><span></span><span></span></div>
  </div>
</header>

<section class="about">
  <h2 class="section-title heading">ABOUT OUR COMPANY</h2>
  <p class="about-text">Velmorix Universal Communication was born out of the desire to offer reliable, affordable phone systems for the small- to medium-sized business. Since 2003, we have offered hosted VOIP PBX and call routing services, but they were bundled with larger IT services. As such, it was only cost-effective for the large corporate client.</p>
  <div class="channel-icons">
    <svg viewBox="0 0 100 90" aria-label="Feeds"><path d="M50 2a43 43 0 1 0 36 66l12 4-8-14A43 43 0 0 0 50 2z" fill="var(--icon-grey)"/><circle cx="40" cy="56" r="5" fill="#fff"/><path d="M36 40a20 20 0 0 1 20 20M36 28a32 32 0 0 1 32 32" stroke="#fff" stroke-width="6" fill="none"/></svg>
    <svg viewBox="0 0 100 90" aria-label="Email"><path d="M50 2a43 43 0 1 0 36 66l12 4-8-14A43 43 0 0 0 50 2z" fill="var(--icon-grey)"/><rect x="28" y="32" width="44" height="28" fill="#fff"/><path d="M28 32l22 17 22-17" stroke="var(--icon-grey)" stroke-width="3" fill="none"/></svg>
    <svg viewBox="0 0 100 90" aria-label="Chat"><path d="M50 2a43 43 0 1 0 36 66l12 4-8-14A43 43 0 0 0 50 2z" fill="var(--icon-grey)"/><ellipse cx="50" cy="44" rx="23" ry="17" fill="#fff"/><path d="M36 56l-6 10 14-6z" fill="#fff"/><circle cx="40" cy="44" r="3" fill="var(--icon-grey)"/><circle cx="50" cy="44" r="3" fill="var(--icon-grey)"/><circle cx="60" cy="44" r="3" fill="var(--icon-grey)"/></svg>
    <svg viewBox="0 0 100 90" aria-label="Web"><path d="M50 2a43 43 0 1 0 36 66l12 4-8-14A43 43 0 0 0 50 2z" fill="var(--icon-grey)"/><circle cx="50" cy="45" r="20" fill="#fff"/><path d="M34 36c10 4 22 4 32 0M32 50c12 5 24 5 36 0M48 25c-6 12-6 28 2 40" stroke="var(--icon-grey)" stroke-width="3" fill="none"/></svg>
    <svg viewBox="0 0 100 90" aria-label="Fax"><path d="M50 2a43 43 0 1 0 36 66l12 4-8-14A43 43 0 0 0 50 2z" fill="var(--icon-grey)"/><rect x="37" y="24" width="26" height="12" fill="#fff"/><rect x="27" y="38" width="46" height="20" rx="3" fill="#fff"/><rect x="37" y="52" width="26" height="14" fill="#fff" stroke="var(--icon-grey)" stroke-width="2"/></svg>
    <svg viewBox="0 0 100 90" aria-label="Mobile"><path d="M50 2a43 43 0 1 0 36 66l12 4-8-14A43 43 0 0 0 50 2z" fill="var(--icon-grey)"/><rect x="38" y="20" width="24" height="48" rx="4" fill="#fff"/><rect x="41" y="26" width="18" height="32" fill="var(--icon-grey)"/><circle cx="50" cy="63" r="2.5" fill="var(--icon-grey)"/></svg>
  </div>
</section>

<section class="why">
  <div class="why-content">
    <h2 class="section-title heading">WHY VELMORIX</h2>
    <div class="why-text">
      <p>Honestly, your office phone system is probably the least sexy thing in your company – the minute the system is down, you’re out of business – so you need a phone system that you can count on every minute of every day.</p>
      <p>But your phone system doesn’t have to be boring, it can look great, too! With a sleek design and customized logos, these phones add a distinctive look sitting on the desk. What is even better, is how good this system makes you look to your customers. Whatever image you want to portray.</p>
    </div>
    <span class="outline-button">LEARN MORE</span>
  </div>
  <div class="tablet">
    <div class="tablet-screen" role="img" aria-label="Network diagram of unified communication linking client offices to redundant telephony providers"></div>
  </div>
</section>

<section class="benefits">
  <h2 class="section-title heading">OUR BENEFITS</h2>
  <div class="benefit" style="left:175px;top:113px">
    <div class="benefit-icon"><svg width="30" height="30" viewBox="0 0 30 30"><path d="M26 4C18 4 12 9 9 16l5 5c7-3 12-9 12-17z" fill="var(--red)"/><path d="M9 16l-5 1 4-6h5zM14 21l-1 5 6-4v-5zM8 22l-4 4" stroke="var(--red)" stroke-width="2" fill="var(--red)"/></svg></div>
    <div class="benefit-name">Quick ROI</div>
    <p class="benefit-text">Lorem ipsum dolor sit amet consectetuer adipiscing elit Nam cursus Morbi ut mi Nullam enim leo egestas</p>
  </div>
  <div class="benefit" style="left:465px;top:113px">
    <div class="benefit-icon"><svg width="30" height="30" viewBox="0 0 30 30"><path d="M15 3l10 4v8c0 6-5 10-10 12C10 25 5 21 5 15V7z" fill="none" stroke="var(--red)" stroke-width="2.5"/><path d="M10 15l4 4 6-7" stroke="var(--red)" stroke-width="2.5" fill="none"/></svg></div>
    <div class="benefit-name">Secure</div>
    <p class="benefit-text">Lorem ipsum dolor sit amet consectetuer adipiscing elit Nam cursus Morbi ut mi Nullam enim leo egestas</p>
  </div>
  <div class="benefit" style="left:754px;top:113px">
    <div class="benefit-icon"><svg width="34" height="30" viewBox="0 0 34 30"><rect x="6" y="6" width="22" height="15" fill="none" stroke="var(--red)" stroke-width="2.5"/><path d="M2 24h30" stroke="var(--red)" stroke-width="2.5"/><path d="M11 16l4-4 3 3 5-5" stroke="var(--red)" stroke-width="2" fill="none"/></svg></div>
    <div class="benefit-name">Easy Installation</div>
    <p class="benefit-text">Lorem ipsum dolor sit amet consectetuer adipiscing elit Nam cursus Morbi ut mi Nullam enim leo egestas</p>
  </div>
  <div class="benefit" style="left:175px;top:221px">
    <div class="benefit-icon"><svg width="30" height="30" viewBox="0 0 30 30"><rect x="4" y="16" width="10" height="10" fill="none" stroke="var(--red)" stroke-width="2.5" stroke-dasharray="3 2"/><path d="M12 18L24 6M17 6h7v7" stroke="var(--red)" stroke-width="2.5" fill="none"/></svg></div>
    <div class="benefit-name">Expandable</div>
    <p class="benefit-text">Lorem ipsum dolor sit amet consectetuer adipiscing elit Nam cursus Morbi ut mi Nullam enim leo egestas</p>
  </div>
  <div class="benefit" style="left:465px;top:221px">
    <div class="benefit-icon"><svg width="34" height="30" viewBox="0 0 34 30"><circle cx="9" cy="19" r="6" fill="var(--red)"/><circle cx="25" cy="19" r="6" fill="var(--red)"/><path d="M15 18h4M3 17L7 7M31 17L27 7" stroke="var(--red)" stroke-width="2" fill="none"/></svg></div>
    <div class="benefit-name">Intuitive</div>
    <p class="benefit-text">Lorem ipsum dolor sit amet consectetuer adipiscing elit Nam cursus Morbi ut mi Nullam enim leo egestas</p>
  </div>
  <div class="benefit" style="left:754px;top:221px">
    <div class="benefit-icon"><svg width="32" height="32" viewBox="0 0 32 32"><circle cx="16" cy="16" r="8" fill="none" stroke="var(--red)" stroke-width="3"/><path d="M16 2v6M16 24v6M2 16h6M24 16h6M6 6l4 4M22 22l4 4M26 6l-4 4M10 22l-4 4" stroke="var(--red)" stroke-width="3"/><path d="M8 24L24 8" stroke="var(--red)" stroke-width="2.5"/></svg></div>
    <div class="benefit-name">Customized</div>
    <p class="benefit-text">Lorem ipsum dolor sit amet consectetuer adipiscing elit Nam cursus Morbi ut mi Nullam enim leo egestas</p>
  </div>
  <div class="view-all">VIEW ALL</div>
</section>

<section class="features">
  <div class="features-photo" role="img" aria-label="Photo of a young woman in a green jacket using a tablet outdoors"></div>
  <h2 class="section-title heading">OUR FEATURES</h2>
  <ul class="feature-list">
    <li>Integrated Phone services for one desk to 100 and beyond</li>
    <li>Work whereever you or your employees are form home, the office,<br>the beach! Velmorix follow you</li>
    <li>Flexible system designed for the unique needs of your company</li>
    <li>Connect multiple location into one system</li>
    <li>Easy to add one station at a time as your bussiness grows</li>
    <li>Expand employee options by setting up work at home stations</li>
  </ul>
</section>

<section class="newsletter" role="img" aria-label="Photo of hands typing on a laptop keyboard beside a phone">
  <h2 class="section-title heading">NEWSLETTER SUBSCRIBE</h2>
  <p class="newsletter-lead">Lorem ipsum dolor sit amet consectetuer adipiscing elit Nam cursus Morbi ut mi Nullam enim</p>
  <div class="subscribe-form">
    <svg class="mail-glyph" width="18" height="13" viewBox="0 0 18 13"><rect width="18" height="13" fill="#c4c4c4"/><path d="M0 0l9 7 9-7" stroke="#fff" stroke-width="1.5" fill="none"/></svg>
    <span class="field">Email address</span>
    <span class="submit">SUBSCRIBE</span>
  </div>
</section>

<footer class="site-footer">
  <nav class="footer-nav"><a>HOME</a><a>ABOUT</a><a>WHY US</a><a>FEATURES</a><a>ADVANTAGES</a><a>SUPPORT</a></nav>
  <p class="copyright">© 2016 Company Name &nbsp;All right reserved &nbsp;Term of Use</p>
  <div class="social" aria-label="Social links"><span></span><span></span><span></span><span></span></div>
</footer>

</body>
</html>
```